Brightfern Supports

We need an updated website that captures the comprehensive services and supports we provide to persons with developmental disabilities. We need a website design that educates families about the services we provide. We would also need a website that is user-friendly so that we could periodically update training schedules and ongoing programming.

• Thank you for submitting designs.  A few things I am hoping to see offered in the website:
• Front page highlights the services we offer (host homes, family caregiver, day program, employment program, SLS program, supported apartment program, behavior/clinical program)
• Front page also highlights any new programs we want to make prominent:  family caregiver, future restaurant employment openings, etc...
• Interactive Training Calendar
• Employee Resources page (link to carelyn, email login, etc.)
• Uniform provider application for host home providers
• Information on agency - history, goals, etc.
• Contact Information/Location

 

Fun things to include:

• Client Highlights (featuring a client story each month, etc...)
• Employee highlights (featuring a staff member...)
• link to other Brightfern business pages (Brightfern Therapy and Brightfern Restaurant)

```html
<!DOCTYPE html>
<html lang="en">
<head>
<meta charset="utf-8">
<title>Brightfern Supports – About Us</title>
<link href="https://fonts.googleapis.com/css2?family=Raleway:wght@400;500;600;700&family=Lato:wght@400;700&display=swap" rel="stylesheet">
<style>
:root{
  --maroon:#7c1f2f;
  --maroon-dark:#6a1826;
  --topbar:#8b8b8d;
  --footer:#8e8e90;
  --footer-line:#a9a9ab;
  --black:#121212;
  --text:#4a4a4a;
  --heading:#3b3b3b;
  --side-a:#6f6f71;
  --side-b:#8a8a8c;
  --side-light:#b9b9bb;
  --white:#ffffff;
}
*{margin:0;padding:0;box-sizing:border-box}
html,body{width:1035px;height:1200px;overflow:hidden;background:var(--white)}
body{position:relative;font-family:'Raleway',sans-serif;color:var(--text)}

.topbar{position:absolute;left:0;top:0;width:1035px;height:35px;background:var(--topbar)}
.social{position:absolute;left:172px;top:10px;display:flex;gap:9px}
.social span{width:14px;height:14px;border-radius:50%;background:var(--white);opacity:.9}
.top-contact{position:absolute;right:0;top:0;height:35px;display:flex;align-items:center;font-family:'Lato',sans-serif;font-size:8px;letter-spacing:.6px;color:var(--white)}
.top-contact .item{display:flex;align-items:center;gap:5px;padding:0 12px;height:35px}
.top-contact .item+.item{border-left:1px solid #a3a3a5}
.top-contact .search{width:186px}

.header{position:absolute;left:0;top:35px;width:1035px;height:73px;background:var(--white)}
.brand{position:absolute;left:154px;top:20px;display:flex;align-items:center;gap:8px}
.brand .mark{width:22px;height:22px;border-radius:50%;background:var(--maroon)}
.brand .name{font-family:'Raleway',sans-serif;font-weight:700;font-size:17px;color:var(--maroon);line-height:1}
.nav{position:absolute;left:410px;top:0;height:73px;display:flex}
.nav a{display:flex;align-items:center;justify-content:center;text-align:center;height:56px;padding:0 10px;font-family:'Lato',sans-serif;font-weight:700;font-size:7.5px;letter-spacing:.6px;color:var(--maroon);text-decoration:none;text-transform:uppercase;line-height:1.25}
.nav a+a{border-left:1px solid #dedede;margin-top:0}
.nav a.active{background:var(--maroon);color:var(--white);height:73px;margin-top:0;padding:0 15px}

.crumbs{position:absolute;left:0;top:108px;width:1035px;height:21px;background:var(--maroon)}
.crumbs p{position:absolute;left:162px;top:6px;font-family:'Lato',sans-serif;font-weight:700;font-size:8px;color:var(--white)}

.sidebar{position:absolute;left:154px;top:151px;width:153px}
.sidebar h2{height:42px;background:var(--maroon);color:var(--white);font-family:'Raleway',sans-serif;font-weight:600;font-size:15px;text-align:center;line-height:42px;letter-spacing:.5px}
.sidebar ul{list-style:none}
.sidebar li{height:22.5px;line-height:22.5px;padding-left:12px;font-family:'Lato',sans-serif;font-size:7px;color:var(--white);background:var(--side-a)}
.sidebar li:nth-child(even){background:var(--side-b)}
.sidebar li.head{background:var(--side-light);text-align:center;padding-left:0}

.content{position:absolute;left:348px;top:151px;width:554px}
.content h1{text-align:center;font-family:'Raleway',sans-serif;font-weight:700;font-size:16px;color:var(--maroon);letter-spacing:.3px;line-height:22px}
.content h1::after{content:"";display:block;width:78px;height:2px;background:var(--maroon);margin:3px auto 0}
.content h3{font-family:'Raleway',sans-serif;font-weight:700;font-size:12.5px;color:var(--heading);margin:36px 0 26px}
.content p{font-size:11px;line-height:23.3px;color:var(--text);margin-bottom:20px}

.footer{position:absolute;left:0;top:1014px;width:1035px;height:169px;background:var(--footer)}
.col{position:absolute;top:46px;color:var(--white);font-family:'Lato',sans-serif}
.col h4{font-size:7.5px;font-weight:700;letter-spacing:.8px;padding-bottom:6px;border-bottom:1px solid var(--footer-line);margin-bottom:10px}
.col p,.col li{font-size:7px;line-height:14px;list-style:none}
.col-about{left:167px;width:128px}
.col-company{left:361px;width:120px}
.col-news{left:534px;width:148px}
.col-help{left:754px;width:118px}
.signup{margin-top:6px;width:138px;height:12px;background:var(--white);border:1px solid #ccc;font-size:6.5px;color:#999;padding-left:4px;line-height:10px}
.signup-btn{margin-top:3px;width:94px;height:10px;background:var(--maroon);font-size:6px;text-align:center;line-height:10px}
.legal{position:absolute;left:0;top:1183px;width:1035px;height:17px;background:var(--black);color:var(--white);font-family:'Lato',sans-serif;font-weight:700;font-size:8px;letter-spacing:1.4px;text-align:center;line-height:17px}
</style>
</head>
<body>

<div class="topbar">
  <div class="social"><span></span><span></span><span></span><span></span><span></span></div>
  <div class="top-contact">
    <div class="item">24/7 SUPPORT
      <svg width="10" height="10" viewBox="0 0 24 24"><path fill="#fff" d="M6.6 10.8a15 15 0 0 0 6.6 6.6l2.2-2.2a1 1 0 0 1 1-.3 11 11 0 0 0 3.6.6 1 1 0 0 1 1 1V20a1 1 0 0 1-1 1A17 17 0 0 1 3 4a1 1 0 0 1 1-1h3.5a1 1 0 0 1 1 1 11 11 0 0 0 .6 3.6 1 1 0 0 1-.3 1z"/></svg>
      +1 555 014 2290</div>
    <div class="item">
      <svg width="14" height="10" viewBox="0 0 14 10"><rect x=".5" y=".5" width="13" height="9" fill="none" stroke="#fff"/><path d="M.5.5 7 6 13.5.5" fill="none" stroke="#fff"/></svg>
      HELLO@BRIGHTFERN.ORG</div>
    <div class="item search">
      <svg width="10" height="10" viewBox="0 0 10 10"><circle cx="4" cy="4" r="3" fill="none" stroke="#fff" stroke-width="1.4"/><path d="M6.2 6.2 9.3 9.3" stroke="#fff" stroke-width="1.4"/></svg>
      SEARCH</div>
  </div>
</div>

<header class="header">
  <div class="brand"><span class="mark"></span><span class="name">Brightfern Supports</span></div>
  <nav class="nav">
    <a href="#">Services</a>
    <a href="#">Become a<br>provider</a>
    <a href="#" class="active">Programs</a>
    <a href="#">Location</a>
    <a href="#">Community<br>resources</a>
    <a href="#">Support</a>
    <a href="#">Our team</a>
  </nav>
</header>

<div class="crumbs"><p>Home &nbsp;›&nbsp; About Us</p></div>

<aside class="sidebar">
  <h2>LINKS</h2>
  <ul>
    <li class="head">a</li>
    <li>Future Restaurant Employment openings</li>
    <li>Future Restaurant</li>
    <li>Future Restaurant Employment openings</li>
    <li>Future Restaurant</li>
    <li>Future Restaurant Employment openings</li>
    <li>Future Restaurant</li>
    <li>Future Restaurant Employment openings</li>
  </ul>
</aside>

<main class="content">
  <h1>ABOUT US</h1>
  <h3>History</h3>
  <p>Lorem ipsum dolor sit amet, consectetur adipiscing elit. Nulla in molestie libero. Ut et luctus turpis. Sed mattis libero libero, pellentesque tristique metus cursus at. Suspendisse porttitor, libero eu vehicula viverra, tellus justo aliquet felis, eget luctus tellus erat et ligula. Sed id eros fermentum, eleifend nisi nec, ultrices lacus. Praesent adipiscing molestie ante, eget rhoncus tortor. Aliquam vitae dui non nisl tristique tempor porttitor nec dolor. Duis eget purus sem. Vivamus venenatis lorem libero, eget bibendum ante sodales feugiat. Cum sociis natoque penatibus et magnis dis parturient montes, nascetur ridiculus mus. Phasellus dictum nisi eu justo tempus aliquam. Fusce et porttitor nunc.</p>
  <p>Curabitur iaculis sapien imperdiet risus tempor fermentum. Proin quis mauris cursus, venenatis justo ut, faucibus augue. Nunc bibendum in nibh vitae ullamcorper. Fusce sodales posuere lobortis. Etiam a ante quis purus condimentum consectetur pretium quis dui. Sed interdum tellus dui, id auctor erat iaculis ullamcorper. Integer nec libero ac nibh ornare fringilla in ac tellus. Mauris vitae nunc a sapien dictum suscipit. Nam dictum erat in lectus convallis, vitae pellentesque diam tincidunt.</p>
  <h3>Goals</h3>
  <p>Lorem ipsum dolor sit amet, consectetur adipiscing elit. Nulla in molestie libero. Ut et luctus turpis. Sed mattis libero libero, pellentesque tristique metus cursus at. Suspendisse porttitor, libero eu vehicula viverra, tellus justo aliquet felis, eget luctus tellus erat et ligula. Sed id eros fermentum, eleifend nisi nec, ultrices lacus. Praesent adipiscing molestie ante, eget rhoncus tortor. Aliquam vitae dui non nisl tristique tempor porttitor nec dolor. Duis eget purus sem. Vivamus venenatis lorem libero, eget bibendum ante sodales feugiat. Cum sociis natoque penatibus et magnis dis parturient montes, nascetur ridiculus mus. Phasellus dictum nisi eu justo tempus aliquam. Fusce et porttitor nunc.</p>
  <p>Curabitur iaculis sapien imperdiet risus tempor fermentum. Proin quis mauris cursus, venenatis justo ut, faucibus augue. Nunc bibendum in nibh vitae ullamcorper. Fusce sodales posuere lobortis. Etiam a ante quis purus condimentum consectetur pretium quis dui. Sed interdum tellus dui, id auctor erat iaculis ullamcorper. Integer nec libero ac nibh ornare fringilla in ac tellus. Mauris vitae nunc a sapien dictum suscipit. Nam dictum erat in lectus convallis, vitae pellentesque diam tincidunt.</p>
</main>

<footer class="footer">
  <div class="col col-about">
    <h4>ABOUT US</h4>
    <p>18 Alder Row<br>Fernvale, CO 80000<br>Phone: 555-014-2291<br>Fax: 555-014-2292</p>
  </div>
  <div class="col col-company">
    <h4>COMPANY</h4>
    <ul><li>About</li><li>Career</li><li>Media Kit</li><li>Contact Us</li></ul>
  </div>
  <div class="col col-news">
    <h4>SUBSCRIBE TO OUR NEWSLETTER</h4>
    <p>Get new program updates, reports<br>and design news.</p>
    <div class="signup">Email Address</div>
    <div class="signup-btn">Subscribe</div>
  </div>
  <div class="col col-help">
    <h4>HELP &amp; SUPPORT</h4>
    <ul><li>Terms</li><li>Privacy</li><li>Sign Up</li><li>Log In</li></ul>
  </div>
</footer>
<div class="legal">© 2014 &nbsp;ALL RIGHTS RESERVED &nbsp;PRIVACY POLICY</div>

</body>
</html>
```